Adult website business card design

velvorbit.co.uk is an adult product website, our main focus is the Tidecurve range, female sex toys and penis pumps/ enlargers. One of our main points is that we will not be beaten on prices for our products, and we offer free shipping on orders over £30. We would like the colours of the business card to be in keeping with the colours of the website.

Industry/Entity Type

Shipping

Contact Information for Business Card

www.velvorbit.co.uk
support@velvorbit.co.uk

```html
<!DOCTYPE html>
<html lang="en">
<head>
<meta charset="utf-8">
<title>Velvorbit Business Card</title>
<link rel="stylesheet" href="https://fonts.googleapis.com/css2?family=Arimo:wght@400&family=Tinos:wght@400&display=swap">
<style>
  :root {
    --backdrop: #dbfcbd;
    --card: #121112;
    --glow: rgba(105, 105, 105, 0.72);
    --name: #f2f2f2;
    --text: #ffffff;
    --accent: #7cc242;
  }
  html, body {
    margin: 0;
    width: 1200px;
    height: 900px;
    overflow: hidden;
    background: var(--backdrop);
  }
  .stage {
    width: 1200px;
    height: 900px;
    display: flex;
    align-items: center;
    justify-content: center;
    gap: 60px;
  }
  .card {
    position: relative;
    width: 525px;
    height: 300px;
    background: var(--card);
    box-shadow: 0 10px 28px rgba(0, 0, 0, 0.28);
    overflow: hidden;
    font-family: "Arimo", Arial, sans-serif;
  }
  .card-glow {
    position: absolute;
    inset: 0;
    background: radial-gradient(ellipse 40% 46% at var(--gx, 50%) var(--gy, 50%), var(--glow), transparent 100%);
  }
  .brand-name {
    position: absolute;
    margin: 0;
    font-weight: 400;
    color: var(--name);
    letter-spacing: 0.5px;
    line-height: 1;
    white-space: nowrap;
  }
  /* Front */
  .card-front { --gx: 48%; --gy: 46%; }
  .card-front .brand-name {
    left: 70px;
    top: 100px;
    font-size: 72px;
  }
  .tagline {
    position: absolute;
    right: 70px;
    top: 196px;
    margin: 0;
    font-size: 17px;
    color: var(--text);
    white-space: nowrap;
  }
  /* Back */
  .card-back { --gx: 52%; --gy: 48%; }
  .assurances {
    position: absolute;
    top: 34px;
    right: 56px;
    margin: 0;
    padding: 0;
    list-style: none;
    font-family: "Tinos", "Times New Roman", serif;
    font-size: 14px;
    line-height: 1.3;
    text-transform: uppercase;
    color: var(--text);
    text-align: right;
  }
  .card-back .brand-name {
    left: 0;
    right: 0;
    top: 112px;
    text-align: center;
    font-size: 56px;
  }
  .contact {
    position: absolute;
    left: 56px;
    bottom: 36px;
    margin: 0;
    font-style: normal;
    font-size: 19px;
    line-height: 1.35;
    color: var(--accent);
  }
  .contact a { color: inherit; text-decoration: none; display: block; }
</style>
</head>
<body>
  <main class="stage">
    <section class="card card-front" aria-label="Business card front">
      <div class="card-glow"></div>
      <h1 class="brand-name">Velvorbit</h1>
      <p class="tagline">We Will Not Be Beaten on Price</p>
    </section>

    <section class="card card-back" aria-label="Business card back">
      <div class="card-glow"></div>
      <ul class="assurances">
        <li>100% Safe &amp; Secure</li>
        <li>Free Shipping Over £30</li>
        <li>Shop With Confidence</li>
      </ul>
      <h2 class="brand-name">Velvorbit</h2>
      <address class="contact">
        <a href="https://www.velvorbit.co.uk">www.velvorbit.co.uk</a>
        <a href="mailto:support@velvorbit.co.uk">support@velvorbit.co.uk</a>
      </address>
    </section>
  </main>
</body>
</html>
```